Coffeeshop menu for filter tip

We want to have a cannabis (coffeeshop) menu in the size 25mm wide x 60mm wide. Some examples attached.

it must have the following text:
Menu

WEED p/g
Velotrine €16
Cinderfox €14
Tide Rambler €14
Marigolden €16
Grand Pelican €14
Copper Comet €14

HASH p/g
Baltic Ember €12
Harbor Velvet€11
Plum Rova €14
Dusk Maple €10

Target Market(s)

tourist in Amsterdam

Requirements
Nice to have
• cannabis sign leaf
• No Cigarettes allowed symbol

```html
<!DOCTYPE html>
<html lang="en">
<head>
<meta charset="utf-8">
<title>Amsterdam Menu</title>
<link rel="stylesheet" href="https://fonts.googleapis.com/css2?family=Arimo:wght@400;700&family=Archivo+Black&display=swap">
<style>
  :root {
    --board: #333230;
    --accent: #f5a31a;
    --ink: #ffffff;
    --leaf-tone: #242322;
    --sign-red: #e0212b;
    --sign-black: #1a1a1a;
  }
  html, body {
    margin: 0;
    padding: 0;
    width: 1200px;
    height: 2878px;
    overflow: hidden;
    background: var(--board);
  }
  .menu-board {
    position: relative;
    width: 1200px;
    height: 2878px;
    background: var(--board);
    font-family: "Arimo", Arial, sans-serif;
    color: var(--ink);
  }
  .title-frame {
    position: absolute;
    left: 59px;
    top: 71px;
    width: 1094px;
    height: 350px;
    box-sizing: border-box;
    border: 4px solid var(--accent);
  }
  .title-city, .title-menu {
    position: absolute;
    left: 149px;
    width: 907px;
    display: flex;
    justify-content: space-between;
    margin: 0;
  }
  .title-city {
    top: 88px;
    font-weight: 700;
    font-size: 111px;
    line-height: 1;
  }
  .title-menu {
    top: 200px;
    font-family: "Archivo Black", "Arial Black", sans-serif;
    font-size: 226px;
    line-height: 210px;
  }
  .leaf-mark {
    position: absolute;
    width: 340px;
    height: 330px;
    border-radius: 50% 50% 45% 45%;
    background: radial-gradient(ellipse at 50% 50%, var(--leaf-tone) 0%, rgba(36,35,34,0.5) 45%, rgba(51,50,48,0) 70%);
  }
  .leaf-weed { left: 523px; top: 469px; }
  .leaf-hash { left: 517px; top: 1545px; }
  .section-title {
    position: absolute;
    left: 62px;
    margin: 0;
    font-weight: 700;
    font-size: 124px;
    line-height: 1;
    letter-spacing: 14px;
    color: var(--accent);
  }
  .unit-label {
    position: absolute;
    font-weight: 700;
    font-size: 120px;
    line-height: 1;
    letter-spacing: 6px;
    color: var(--accent);
  }
  .price-list {
    position: absolute;
    left: 62px;
    width: 1090px;
    margin: 0;
    padding: 0;
    list-style: none;
  }
  .price-row {
    display: flex;
    height: 124.3px;
    font-size: 96px;
    line-height: 124.3px;
    letter-spacing: 6px;
    white-space: nowrap;
  }
  .item-leader {
    flex: 1;
    overflow: hidden;
    min-width: 0;
  }
  .item-price { padding-left: 6px; }
  .no-smoking {
    position: absolute;
    left: 84px;
    top: 2521px;
    width: 246px;
    height: 246px;
  }
  .house-rule {
    position: absolute;
    left: 394px;
    top: 2609px;
    font-size: 96px;
    line-height: 1;
    letter-spacing: 7px;
    margin: 0;
  }
</style>
</head>
<body>
<main class="menu-board">
  <header class="title-frame"></header>
  <h1 class="title-city" aria-label="Amsterdam"><span>A</span><span>M</span><span>S</span><span>T</span><span>E</span><span>R</span><span>D</span><span>A</span><span>M</span></h1>
  <p class="title-menu" aria-label="Menu"><span>M</span><span>E</span><span>N</span><span>U</span></p>

  <div class="leaf-mark leaf-weed" role="img" aria-label="Faint cannabis leaf decoration"></div>
  <h2 class="section-title" style="top:571px;">WEED</h2>
  <span class="unit-label" style="left:912px; top:546px;">p/g</span>
  <ul class="price-list" style="top:769px;">
    <li class="price-row"><span>Velotrine</span><span class="item-leader">..............................</span><span class="item-price">€16</span></li>
    <li class="price-row"><span>Cinderfox</span><span class="item-leader">..............................</span><span class="item-price">€14</span></li>
    <li class="price-row"><span>Tide Rambler</span><span class="item-leader">..............................</span><span class="item-price">€14</span></li>
    <li class="price-row"><span>Marigolden</span><span class="item-leader">..............................</span><span class="item-price">€16</span></li>
    <li class="price-row"><span>Grand Pelican</span><span class="item-leader">..............................</span><span class="item-price">€14</span></li>
    <li class="price-row"><span>Copper Comet</span><span class="item-leader">..............................</span><span class="item-price">€14</span></li>
  </ul>

  <div class="leaf-mark leaf-hash" role="img" aria-label="Faint cannabis leaf decoration"></div>
  <h2 class="section-title" style="top:1669px;">HASH</h2>
  <span class="unit-label" style="left:918px; top:1646px;">p/g</span>
  <ul class="price-list" style="top:1865px;">
    <li class="price-row"><span>Baltic Ember</span><span class="item-leader">..............................</span><span class="item-price">€12</span></li>
    <li class="price-row"><span>Harbor Velvet</span><span class="item-leader">..............................</span><span class="item-price">€11</span></li>
    <li class="price-row"><span>Plum Rova</span><span class="item-leader">..............................</span><span class="item-price">€14</span></li>
    <li class="price-row"><span>Dusk Maple</span><span class="item-leader">..............................</span><span class="item-price">€10</span></li>
  </ul>

  <svg class="no-smoking" viewBox="0 0 246 246" role="img" aria-label="No smoking sign">
    <circle cx="123" cy="123" r="112" fill="var(--ink)" stroke="var(--sign-red)" stroke-width="20"/>
    <rect x="40" y="142" width="130" height="26" fill="var(--sign-black)"/>
    <rect x="176" y="142" width="7" height="26" fill="var(--sign-black)"/>
    <rect x="189" y="142" width="7" height="26" fill="var(--sign-black)"/>
    <path d="M150 40 c-20 10 -10 30 5 35 c20 6 25 25 30 60" fill="none" stroke="var(--sign-black)" stroke-width="8" stroke-linecap="round"/>
    <path d="M172 50 c-10 12 5 22 15 30 c10 10 10 30 8 55" fill="none" stroke="var(--sign-black)" stroke-width="7" stroke-linecap="round"/>
    <line x1="44" y1="44" x2="202" y2="202" stroke="var(--sign-red)" stroke-width="20"/>
  </svg>
  <p class="house-rule">No Cigarettes</p>
</main>
</body>
</html>
```